Bramfield Animal Hospital brochure

We have found that our current clients do not know all of the services that we offer so we want to make a hospital brochure to make our services more known. Our website has all of our services listed but we find that clients aren't looking at our website as much as we would like so we are hoping a hospital brochure can sum up our main services and maybe lead to more people visiting our website. Our hospital colors are blue and maroon and our moto is "Outstanding Medicine, Extraordinary Service." Some of the service we would like to promote more include digital x-ray, ultrasounds, echocardiograms, laser therapy and dentals. We also offer after hours emergency care but only to our current clients. You can find more services listed on our website We are in a small town so we want a personal yet professional feel.

Feel free to visit our website to get a better feel for our business https://thecorvelpets.com/

• 6-8 panel brochure
• I included some photos from around the hospital. If you feel that you can make a few work in the brochure then great but don't feel obligated to.

```html
<!DOCTYPE html>
<html lang="en">
<head>
<meta charset="utf-8">
<title>Bramfield Animal Hospital Brochure</title>
<link rel="stylesheet" href="https://fonts.googleapis.com/css2?family=Oswald:wght@300;500;600&family=Mulish:wght@400;600&display=swap">
<style>
:root{
  --maroon:#8c1a1f;
  --ink:#2b2b2b;
  --paper:#ffffff;
  --stage:#8a8a8a;
  --wall-top:#a98a8e;
  --wall-bottom:#7d6468;
  --fleece-light:#6f6f70;
  --fleece-dark:#3e3e40;
  --map-green:#cfe8d6;
}
*{box-sizing:border-box;margin:0;padding:0}
html,body{width:1200px;height:1185px;overflow:hidden;background:var(--stage)}
.canvas{position:relative;width:1200px;height:1185px}
.spread{position:absolute;left:200px;width:900px;height:633px;background:var(--paper);
  transform:scale(.8889);transform-origin:0 0;overflow:hidden;box-shadow:0 4px 14px rgba(0,0,0,.25)}
.spread--outside{top:15px}
.spread--inside{top:607px}
.spread svg.bg{position:absolute;inset:0}
.headline{position:absolute;left:40px;top:58px;width:220px;text-align:center;font-family:"Oswald",sans-serif;
  font-weight:600;color:var(--maroon);line-height:1.05;text-transform:uppercase}
.headline span{display:block}
.h-sm{font-size:38px;font-weight:500}
.h-md{font-size:60px}
.h-xs{font-size:33px;font-weight:500}
.h-lg{font-size:72px}
.body-copy{position:absolute;font-family:"Mulish",sans-serif;color:var(--ink);text-align:justify}
.intro{left:27px;top:403px;width:247px;font-size:10.6px;line-height:1.36}
.contact{position:absolute;left:376px;top:510px;width:160px;text-align:center;font-family:"Mulish",sans-serif;font-size:11px;color:var(--ink);line-height:1.3}
.contact-icons{display:flex;justify-content:center;gap:3px;margin-bottom:5px}
.brand{position:absolute;left:690px;top:500px;display:flex;align-items:center;gap:8px}
.brand-dot{width:34px;height:34px;border-radius:50%;background:var(--maroon)}
.brand-name{font-family:"Oswald",sans-serif;font-weight:500;font-size:20px;line-height:1.1;color:var(--maroon);text-transform:uppercase}
.emergency-title{position:absolute;left:27px;top:345px;font-family:"Oswald",sans-serif;color:var(--maroon);line-height:1}
.emergency-title .big{display:block;font-size:72px;font-weight:600}
.emergency-title .sub{display:block;font-size:40px;font-weight:300}
.emergency-copy{left:27px;top:468px;width:250px;font-size:9.6px;line-height:12.4px}
.services-title{position:absolute;left:347px;top:345px;font-family:"Oswald",sans-serif;font-weight:600;font-size:26px;color:var(--maroon);line-height:1.2}
.service{position:absolute;display:flex;align-items:center;gap:9px;font-family:"Mulish",sans-serif;font-size:11.5px;color:var(--ink);line-height:1.3;width:145px}
.service svg{flex:0 0 34px}
</style>
</head>
<body>
<div class="canvas">

<section class="spread spread--outside">
  <svg class="bg" width="900" height="633" viewBox="0 0 900 633">
    <defs>
      <linearGradient id="wall" x1="0" y1="0" x2="1" y2="1">
        <stop offset="0" stop-color="var(--wall-top)"/><stop offset="1" stop-color="var(--wall-bottom)"/>
      </linearGradient>
    </defs>
    <path role="img" aria-label="Photo: veterinarian holding an orange cat against a mauve wall" fill="url(#wall)"
      d="M0,0H900V285C830,400 700,440 560,420C470,408 420,330 300,325C180,320 90,335 0,350Z"/>
    <path fill="var(--maroon)" d="M0,350C90,335 180,320 300,325C360,327 400,335 430,345L430,362C400,352 360,344 300,342C180,338 90,355 0,388Z"/>
    <path fill="var(--maroon)" d="M560,420C700,440 830,400 900,285V318C830,430 700,470 560,448C540,445 520,438 505,430L510,410C525,416 542,418 560,420Z"/>
    <path fill="var(--maroon)" d="M0,603C300,612 600,606 900,583V633H0Z"/>
    <circle cx="456" cy="401" r="112" fill="#fff"/>
    <circle role="img" aria-label="Street map showing the hospital location" cx="456" cy="401" r="106" fill="var(--map-green)"/>
  </svg>

  <h1 class="headline">
    <span class="h-sm">Outstanding</span>
    <span class="h-md">Medicine</span>
    <span class="h-xs">Extraordinary</span>
    <span class="h-lg">Service</span>
  </h1>

  <p class="body-copy intro">We built Bramfield Animal Hospital for you. It is so important to us that you can walk into an environment where you feel you are always put first, and where the little things have been thought of to make this a truly wonderful experience. We want to make your life easier. We offer evening hours, drop-offs, and house call appointments. And existing clients get access to 24 hour emergency care. Because we are always looking out for you.</p>

  <div class="contact">
    <div class="contact-icons">
      <svg width="14" height="14" viewBox="0 0 14 14"><circle cx="7" cy="7" r="6" fill="none" stroke="var(--maroon)" stroke-width="1.3"/><path d="M4.6,4.2l1.3-.4.7,1.6-.8.6c.4.8.9 1.3 1.7 1.7l.6-.8 1.6.7-.4 1.3c-2.5.1-4.8-2.2-4.7-4.7z" fill="var(--maroon)"/></svg>
      <svg width="14" height="14" viewBox="0 0 14 14"><circle cx="7" cy="7" r="6" fill="var(--maroon)"/><rect x="3.8" y="4.8" width="6.4" height="4.4" fill="#fff"/><path d="M3.8,4.8L7,7.3 10.2,4.8" fill="none" stroke="var(--maroon)" stroke-width=".8"/></svg>
      <svg width="14" height="14" viewBox="0 0 14 14"><circle cx="7" cy="7" r="6" fill="none" stroke="var(--maroon)" stroke-width="1.3"/><circle cx="7" cy="7" r="3" fill="none" stroke="var(--maroon)" stroke-width=".9"/><path d="M4,7H10M7,4V10" stroke="var(--maroon)" stroke-width=".8"/></svg>
    </div>
    802-555-0148<br>info@thecorvelpets.com<br>info@thecorvelpets.com
  </div>

  <div class="brand">
    <span class="brand-dot"></span>
    <span class="brand-name">Bramfield<br>Animal Hospital</span>
  </div>
</section>

<section class="spread spread--inside">
  <svg class="bg" width="900" height="633" viewBox="0 0 900 633">
    <defs>
      <linearGradient id="fleece" x1="0" y1="0" x2="1" y2="1">
        <stop offset="0" stop-color="var(--fleece-light)"/><stop offset=".55" stop-color="#b9753a"/><stop offset="1" stop-color="var(--fleece-dark)"/>
      </linearGradient>
    </defs>
    <path role="img" aria-label="Photo: orange cat curled up on a grey fleece blanket" fill="url(#fleece)"
      d="M0,0H900V230C780,228 660,285 500,305C320,328 110,300 0,212Z"/>
    <path fill="var(--maroon)" d="M300,318C380,322 440,312 500,305C660,285 780,228 900,230V252C780,250 660,307 500,326C420,334 350,330 300,318Z"/>
    <path fill="var(--maroon)" d="M0,603C300,612 600,606 900,583V633H0Z"/>
  </svg>

  <h2 class="emergency-title"><span class="big">24 HOUR</span><span class="sub">EMERGENCY CARE</span></h2>
  <p class="body-copy emergency-copy">We keep a veterinarian on call 24 hours a day for emergency services. In order to treat your pet as quickly as possible, we restrict after hours emergency care to current clients. If you are not a current client and may be experiencing an after hours pet emergency, please contact your regular veterinarian or Valley Regional Animal Emergency Clinic at (518) 555-0172.</p>

  <h3 class="services-title">SERVICES WE OFFER</h3>

  <div class="service" style="left:347px;top:408px"><svg width="34" height="34" viewBox="0 0 34 34"><circle cx="17" cy="17" r="16" fill="none" stroke="var(--maroon)" stroke-width="1.5"/><path d="M9,18h4l2-5 3,9 2-4h5" fill="none" stroke="var(--maroon)" stroke-width="1.6"/></svg>EchoCardio<br>Grams</div>
  <div class="service" style="left:347px;top:453px"><svg width="34" height="34" viewBox="0 0 34 34"><circle cx="17" cy="17" r="16" fill="none" stroke="var(--maroon)" stroke-width="1.5"/><circle cx="17" cy="17" r="4" fill="none" stroke="var(--maroon)" stroke-width="1.6"/><path d="M17,8v4M17,22v4M8,17h4M22,17h4" stroke="var(--maroon)" stroke-width="1.6"/></svg>Cold Laser<br>Therapy</div>
  <div class="service" style="left:347px;top:498px"><svg width="34" height="34" viewBox="0 0 34 34"><circle cx="17" cy="17" r="16" fill="none" stroke="var(--maroon)" stroke-width="1.5"/><rect x="11" y="10" width="12" height="14" fill="none" stroke="var(--maroon)" stroke-width="1.6"/><path d="M17,12v10M13,15h8M13,19h8" stroke="var(--maroon)" stroke-width="1.2"/></svg>Digital<br>X-Ray</div>
  <div class="service" style="left:347px;top:543px"><svg width="34" height="34" viewBox="0 0 34 34"><circle cx="17" cy="17" r="16" fill="none" stroke="var(--maroon)" stroke-width="1.5"/><path d="M15,9h4v6h6v4h-6v6h-4v-6h-6v-4h6z" fill="var(--maroon)"/></svg>Emergency<br>Care</div>

  <div class="service" style="left:473px;top:408px"><svg width="34" height="34" viewBox="0 0 34 34"><circle cx="17" cy="17" r="16" fill="none" stroke="var(--maroon)" stroke-width="1.5"/><circle cx="17" cy="17" r="8" fill="none" stroke="var(--maroon)" stroke-width="1.6"/><path d="M11,11l12,12" stroke="var(--maroon)" stroke-width="1.6"/></svg>Flea and<br>Tick Prevention</div>
  <div class="service" style="left:473px;top:453px"><svg width="34" height="34" viewBox="0 0 34 34"><circle cx="17" cy="17" r="16" fill="none" stroke="var(--maroon)" stroke-width="1.5"/><path d="M17,25C9,19 8,15 10,12c2-3 5-2 7,1 2-3 5-4 7-1 2,3 1,7-7,13z" fill="var(--maroon)"/></svg>Heartworm<br>Preventative</div>
  <div class="service" style="left:473px;top:498px"><svg width="34" height="34" viewBox="0 0 34 34"><circle cx="17" cy="17" r="16" fill="none" stroke="var(--maroon)" stroke-width="1.5"/><path d="M8,18l9-8 9,8M11,16v9h12v-9" fill="none" stroke="var(--maroon)" stroke-width="1.8"/></svg>In-House<br>Laboratory</div>
  <div class="service" style="left:473px;top:543px"><svg width="34" height="34" viewBox="0 0 34 34"><circle cx="17" cy="17" r="16" fill="none" stroke="var(--maroon)" stroke-width="1.5"/><rect x="15" y="15" width="11" height="5" rx="2" fill="none" stroke="var(--maroon)" stroke-width="1.4"/><path d="M9,13a6,6 0 0 1 0,9M12,14.5a3,3 0 0 1 0,6" fill="none" stroke="var(--maroon)" stroke-width="1.3"/></svg>Micro-<br>chipping</div>

  <div class="service" style="left:615px;top:318px"><svg width="34" height="34" viewBox="0 0 34 34"><circle cx="17" cy="17" r="16" fill="none" stroke="var(--maroon)" stroke-width="1.5"/><circle cx="17" cy="17" r="8" fill="none" stroke="var(--maroon)" stroke-width="1.4"/><path d="M17,21C13,18 13,16 14,15c1-1 2-1 3,1 1-2 2-2 3-1 1,1 1,3-3,6z" fill="var(--maroon)"/></svg>End-Of-Life<br>Care</div>
  <div class="service" style="left:615px;top:363px"><svg width="34" height="34" viewBox="0 0 34 34"><circle cx="17" cy="17" r="16" fill="none" stroke="var(--maroon)" stroke-width="1.5"/><ellipse cx="17" cy="18" rx="5" ry="6" fill="none" stroke="var(--maroon)" stroke-width="1.5"/><path d="M12,14l-3-2M22,14l3-2M12,19h-4M22,19h4M13,23l-3,3M21,23l3,3" stroke="var(--maroon)" stroke-width="1.2"/></svg>Parasite<br>Testing</div>
  <div class="service" style="left:615px;top:408px"><svg width="34" height="34" viewBox="0 0 34 34"><circle cx="17" cy="17" r="16" fill="none" stroke="var(--maroon)" stroke-width="1.5"/><rect x="10" y="11" width="14" height="12" fill="none" stroke="var(--maroon)" stroke-width="1.5"/><circle cx="14" cy="16" r="1.3" fill="var(--maroon)"/><circle cx="20" cy="19" r="1.3" fill="var(--maroon)"/><circle cx="17" cy="15" r="1" fill="var(--maroon)"/></svg>Allergy and<br>Dermatology</div>
  <div class="service" style="left:615px;top:453px"><svg width="34" height="34" viewBox="0 0 34 34"><circle cx="17" cy="17" r="16" fill="none" stroke="var(--maroon)" stroke-width="1.5"/><path d="M11,22c2-8 10-11 13-8-3,0-4,2-4,4 0,4-5,5-9,4z" fill="none" stroke="var(--maroon)" stroke-width="1.5"/></svg>Avian<br>Care</div>
  <div class="service" style="left:615px;top:498px"><svg width="34" height="34" viewBox="0 0 34 34"><circle cx="17" cy="17" r="16" fill="none" stroke="var(--maroon)" stroke-width="1.5"/><path d="M17,9v17M12,13l5,3 5-3M12,19l5,3 5-3" fill="none" stroke="var(--maroon)" stroke-width="1.6"/></svg>Senior<br>Wellness</div>
  <div class="service" style="left:615px;top:543px"><svg width="34" height="34" viewBox="0 0 34 34"><circle cx="17" cy="17" r="16" fill="none" stroke="var(--maroon)" stroke-width="1.5"/><path d="M11,24l7-7M16,12l6,6-3,3-6-6z" fill="none" stroke="var(--maroon)" stroke-width="1.6"/></svg>Ultra<br>Sound</div>

  <div class="service" style="left:742px;top:318px"><svg width="34" height="34" viewBox="0 0 34 34"><circle cx="17" cy="17" r="16" fill="none" stroke="var(--maroon)" stroke-width="1.5"/><circle cx="17" cy="18" r="6" fill="none" stroke="var(--maroon)" stroke-width="1.5"/><path d="M14,11h6" stroke="var(--maroon)" stroke-width="1.5"/></svg>Nutritional<br>Consultations</div>
  <div class="service" style="left:742px;top:363px"><svg width="34" height="34" viewBox="0 0 34 34"><circle cx="17" cy="17" r="16" fill="none" stroke="var(--maroon)" stroke-width="1.5"/><circle cx="14" cy="15" r="2.5" fill="none" stroke="var(--maroon)" stroke-width="1.3"/><circle cx="21" cy="19" r="3" fill="none" stroke="var(--maroon)" stroke-width="1.3"/><path d="M10,24h15" stroke="var(--maroon)" stroke-width="1.3"/></svg>Puppy and<br>Kitten Care</div>
  <div class="service" style="left:742px;top:408px"><svg width="34" height="34" viewBox="0 0 34 34"><circle cx="17" cy="17" r="16" fill="none" stroke="var(--maroon)" stroke-width="1.5"/><path d="M13,10l11,11-3,3-11-11zM16,16l-4,4" fill="none" stroke="var(--maroon)" stroke-width="1.5"/></svg>Blood Tests and<br>Urine Screening</div>
  <div class="service" style="left:742px;top:453px"><svg width="34" height="34" viewBox="0 0 34 34"><circle cx="17" cy="17" r="16" fill="none" stroke="var(--maroon)" stroke-width="1.5"/><path d="M11,11c2-1 4,0 6,1 2-1 4-2 6-1 2,2 0,8-1,13h-2l-1-5h-4l-1,5h-2c-1-5-3-11-1-13z" fill="var(--maroon)"/></svg>Canine and Feline<br>Dental Care</div>
  <div class="service" style="left:742px;top:498px"><svg width="34" height="34" viewBox="0 0 34 34"><circle cx="17" cy="17" r="16" fill="none" stroke="var(--maroon)" stroke-width="1.5"/><path d="M10,22h14M12,22v-5h10v5M15,17v-4h4v4" fill="none" stroke="var(--maroon)" stroke-width="1.5"/></svg>Soft Tissue<br>Surgery</div>
</section>

</div>
</body>
</html>
```